Business Card Design

Looking for a professional looking business card for a carpentry/construction business that deals with renovations, extensions, homes, and anything carpentry based in Northern Australia. Would like to incorporate the attached logo with backgrounds of white, grey or maybe a close up of timber/wood grain. Thanks

Industry/Entity Type

Carpentry

Contact Information for Business Card

Dean Carlow, Owner, Po Box 2674 Katherine NT 0851, dean-carlow@fernmail.example, 0419563072, Builders Number: 293417CR

Requirements
Should not have
• Power tools/hand tools related to carpentry

```html
<!DOCTYPE html>
<html lang="en">
<head>
<meta charset="utf-8">
<title>Carlow Carpentry – Business Card</title>
<link href="https://fonts.googleapis.com/css2?family=Open+Sans:wght@400;600&display=swap" rel="stylesheet">
<style>
  :root {
    --backdrop-centre: #f7f7f7;
    --backdrop-edge: #dfe0e0;
    --card-white: #ffffff;
    --card-blue: #1076bd;
    --brand-blue: #1f5ea8;
    --dash-on-white: #1a7cc4;
    --dash-on-blue: #ffffff;
    --text-light: #ffffff;
  }
  html, body {
    margin: 0;
    padding: 0;
    width: 1200px;
    height: 1000px;
    overflow: hidden;
  }
  body {
    background: radial-gradient(ellipse at 50% 50%, var(--backdrop-centre) 0%, var(--backdrop-edge) 75%);
    font-family: "Open Sans", sans-serif;
    position: relative;
  }
  .business-card {
    position: absolute;
    left: 307px;
    top: 350px;
    width: 573px;
    height: 296px;
    border-radius: 10px;
    overflow: hidden;
    background: var(--card-white);
  }
  .card-band {
    position: absolute;
    left: 0;
    top: 148px;
    width: 100%;
    height: 148px;
    background: var(--card-blue);
  }
  .stitch-frame {
    position: absolute;
    left: 0;
    top: 0;
  }
  .brand-name {
    position: absolute;
    left: 0;
    right: 0;
    top: 52px;
    display: flex;
    justify-content: center;
    align-items: center;
    gap: 12px;
    color: var(--brand-blue);
    font-weight: 600;
    font-size: 38px;
    line-height: 1;
    letter-spacing: 0.5px;
  }
  .brand-mark {
    width: 14px;
    height: 14px;
    background: var(--brand-blue);
  }
  .holder-name {
    position: absolute;
    right: 49px;
    top: 171px;
    margin: 0;
    color: var(--text-light);
    font-weight: 400;
    font-size: 25px;
    line-height: 1;
  }
  .contact-list {
    position: absolute;
    left: 27px;
    top: 189px;
    margin: 0;
    padding: 0;
    list-style: none;
    color: var(--text-light);
    font-size: 14.5px;
    line-height: 22px;
  }
</style>
</head>
<body>
  <div class="business-card">
    <div class="card-band"></div>

    <svg class="stitch-frame" width="573" height="296" viewBox="0 0 573 296" aria-hidden="true">
      <defs>
        <clipPath id="upper-half"><rect x="0" y="0" width="573" height="148"/></clipPath>
        <clipPath id="lower-half"><rect x="0" y="148" width="573" height="148"/></clipPath>
      </defs>
      <rect x="15.5" y="10.5" width="544" height="275" rx="8" fill="none"
            stroke="var(--dash-on-white)" stroke-width="2" stroke-dasharray="9 6"
            clip-path="url(#upper-half)"/>
      <rect x="15.5" y="10.5" width="544" height="275" rx="8" fill="none"
            stroke="var(--dash-on-blue)" stroke-width="2" stroke-dasharray="9 6"
            clip-path="url(#lower-half)"/>
    </svg>

    <div class="brand-name">
      <span class="brand-mark"></span>
      <span>Carlow Carpentry</span>
    </div>

    <p class="holder-name">Dean Carlow</p>

    <ul class="contact-list">
      <li>0419563072</li>
      <li>dean-carlow@fernmail.example</li>
      <li>Builders Number: 293417CR</li>
      <li>Po Box 2674 Katherine NT 0851</li>
    </ul>
  </div>
</body>
</html>
```